Business card design needed

am looking for a fun and funky design to match our moto, seriously fun swimwear and fashion for girls.

We manufacture and retail girls swimwear and fashion in Australia. Our designs are fun loving and funky. I would like to use bright fuschia to match our website www.breezyplum.com.au. We target a higher end market so need it to reflect this.

Industry/Entity Type

Fashion

Contact Information for Business Card

Breezy Plum logo,
Maddie Lorne
(07) 35517204
admin@breezyplum.com.au
www.breezyplum.com.au

Logo Text

Breezy Plum

```html
<!DOCTYPE html>
<html lang="en">
<head>
<meta charset="utf-8">
<title>Breezy Plum – Business Card</title>
<link rel="stylesheet" href="https://fonts.googleapis.com/css2?family=Barlow:wght@300;400&display=swap">
<style>
  :root {
    --page: #ffffff;
    --card-white: #ffffff;
    --fuchsia: #e619dc;
    --text-light: #ffffff;
  }
  html, body {
    margin: 0;
    padding: 0;
    width: 1200px;
    height: 900px;
    overflow: hidden;
    background: var(--page);
  }
  .canvas {
    position: relative;
    width: 1200px;
    height: 900px;
  }
  .business-card {
    position: absolute;
    left: 69px;
    top: 143px;
    width: 1062px;
    height: 614px;
    background: var(--card-white);
    overflow: hidden;
    font-family: "Barlow", sans-serif;
  }
  .colour-sweep {
    position: absolute;
    inset: 0;
    width: 100%;
    height: 100%;
  }
  .colour-sweep path { fill: var(--fuchsia); }
  .brand-name {
    position: absolute;
    left: 56px;
    top: 80px;
    margin: 0;
    font-weight: 300;
    font-size: 104px;
    line-height: 1;
    color: var(--fuchsia);
    letter-spacing: 1px;
  }
  .contact {
    position: absolute;
    right: 83px;
    top: 380px;
    text-align: right;
    color: var(--text-light);
    font-weight: 300;
  }
  .contact-name {
    margin: 0 0 6px;
    font-size: 46px;
    font-weight: 300;
    line-height: 1.1;
  }
  .contact-line {
    margin: 0;
    font-size: 31px;
    line-height: 39px;
    letter-spacing: 1px;
  }
</style>
</head>
<body>
  <main class="canvas">
    <section class="business-card">
      <svg class="colour-sweep" viewBox="0 0 1062 614" preserveAspectRatio="none" role="img" aria-label="Fuchsia sweep with faint swirl decoration">
        <path d="M0,519 C400,515 800,330 934,0 L1062,0 L1062,614 L0,614 Z"/>
      </svg>
      <h1 class="brand-name">Breezy Plum</h1>
      <address class="contact" style="font-style: normal;">
        <p class="contact-name">Maddie Lorne</p>
        <p class="contact-line">(07) 35517204</p>
        <p class="contact-line">admin@breezyplum.com.au</p>
        <p class="contact-line">www.breezyplum.com.au</p>
      </address>
    </section>
  </main>
</body>
</html>
```